BUSINESS CARD - HALVERDINE RURAL SERVICES

I would like to create a business card for my fertilizer spreading business. I would like to incorporate my existing logo and also a description of the services offered. The business card will be given to farmers so must be kept simple but effective. It will also be left in stores so much also be eye catching in order to stand out from other cards.

Target Market(s)

FARMERS

Requirements
Must have
• FRONT OF CARD = EXISTING LOGO + "CUSTOMISED SPREADING" below the logo

REAR Of CARD = SERVICES OFFERED AND CONTACT DETAILS

- Bulk fertilizer including Lime, Gypsum, Manure & Compost
- Granular fertilizer including Single Super, Urea, Granovel, & Custom Blends
- Modern equipment - Autosteer & Variable Rate Capable
- Friendly & Reliable Service
- Contact Gus: 0471 502 318
Nice to have
• utilize same color scheme as existing logo

```html
<!DOCTYPE html>
<html lang="en">
<head>
<meta charset="utf-8">
<title>Halverdine Rural Services – Business Card</title>
<link href="https://fonts.googleapis.com/css2?family=Open+Sans:wght@400;600;700&family=Roboto:wght@500&display=swap" rel="stylesheet">
<style>
  :root {
    --backdrop: #e4e4e4;
    --card-light: #f4f4f4;
    --card-dark: #545454;
    --ink: #545454;
    --orange: #f0962a;
    --white: #ffffff;
    --emblem-hi: #9a9a9a;
    --emblem-lo: #3c3c3c;
  }
  * { box-sizing: border-box; margin: 0; padding: 0; }
  html, body { width: 1200px; height: 960px; overflow: hidden; }
  body {
    background: var(--backdrop);
    font-family: "Open Sans", Arial, sans-serif;
    position: relative;
  }
  .card {
    position: absolute;
    left: 309px;
    width: 584px;
    height: 358px;
  }
  .card--front { top: 101px; background: var(--card-light); }
  .card--back { top: 505px; background: var(--card-dark); color: var(--white); }

  /* Front */
  .brand-mark {
    position: absolute;
    left: 207px; top: 76px;
    width: 150px; height: 150px;
    border-radius: 50%;
    background: var(--ink);
  }
  .brand-name {
    position: absolute;
    left: 0; right: 0; top: 226px;
    text-align: center;
    font-family: "Roboto", Arial, sans-serif;
    font-weight: 500;
    font-size: 36px;
    letter-spacing: -0.5px;
    color: var(--ink);
  }
  .tagline {
    position: absolute;
    left: 0; right: 0; top: 312px;
    text-align: center;
    font-weight: 700;
    font-size: 14.5px;
    letter-spacing: 1.4px;
    color: var(--ink);
  }

  /* Back */
  .emblem {
    position: absolute;
    left: 25px; top: 50px;
    width: 258px; height: 270px;
    border-radius: 50%;
    background: radial-gradient(circle at 40% 30%, var(--emblem-hi), var(--emblem-lo) 75%);
  }
  .contact {
    position: absolute;
    left: 58px; top: 88px;
    width: 180px;
    text-align: center;
  }
  .contact__name {
    font-size: 29px;
    font-weight: 700;
    color: var(--orange);
    line-height: 1.1;
  }
  .contact__phone {
    margin-top: 4px;
    font-size: 18px;
    font-weight: 400;
    white-space: nowrap;
    display: flex; align-items: center; justify-content: center; gap: 5px;
  }
  .services {
    position: absolute;
    left: 328px; top: 54px;
    list-style: none;
    font-size: 15.8px;
    line-height: 19.5px;
  }
  .services li {
    position: relative;
    padding-left: 16px;
    margin-bottom: 11px;
    white-space: nowrap;
  }
  .services li svg { position: absolute; left: 0; top: 4px; }
  .services strong { font-weight: 700; }
</style>
</head>
<body>

<section class="card card--front">
  <div class="brand-mark" aria-hidden="true"></div>
  <h1 class="brand-name">Halverdine Rural Services</h1>
  <p class="tagline">CUSTOMISED SPREADING</p>
</section>

<section class="card card--back">
  <div class="emblem" aria-hidden="true"></div>
  <div class="contact">
    <p class="contact__name">GUS</p>
    <p class="contact__phone">
      <svg width="19" height="19" viewBox="0 0 18 18" aria-hidden="true">
        <circle cx="9" cy="9" r="8" fill="none" stroke="#f0962a" stroke-width="1.5"/>
        <path d="M6 5.2c.5-.4 1-.3 1.3.2l.6 1.1c.2.4.1.8-.2 1l-.4.3c.4.9 1 1.6 1.9 2.1l.3-.4c.3-.3.7-.3 1-.1l1.1.7c.4.3.5.8.1 1.2-.8.9-1.8.9-2.8.3-1.5-.8-2.7-2.1-3.3-3.7-.3-1-.3-1.9.4-2.7z" fill="#f0962a"/>
      </svg>
      0471 502 318
    </p>
  </div>

  <ul class="services">
    <li>
      <svg width="11" height="11" viewBox="0 0 11 11" aria-hidden="true"><path d="M1 10C1 4 5 1 10 1 10 6 7 10 1 10z" fill="#f0962a"/></svg>
      <strong>Bulk Fertilizer</strong><br>including Lime, Gypsum,<br>Manure &amp; Compost
    </li>
    <li>
      <svg width="11" height="11" viewBox="0 0 11 11" aria-hidden="true"><path d="M1 10C1 4 5 1 10 1 10 6 7 10 1 10z" fill="#f0962a"/></svg>
      <strong>Granular Fertilizer</strong><br>including Single Super,<br>Urea, Granovel<br>&amp; Custom Blends
    </li>
    <li>
      <svg width="11" height="11" viewBox="0 0 11 11" aria-hidden="true"><path d="M1 10C1 4 5 1 10 1 10 6 7 10 1 10z" fill="#f0962a"/></svg>
      <strong>Modern Equipment</strong><br>Autosteer &amp; Variable<br>Rate Capable
    </li>
    <li>
      <svg width="11" height="11" viewBox="0 0 11 11" aria-hidden="true"><path d="M1 10C1 4 5 1 10 1 10 6 7 10 1 10z" fill="#f0962a"/></svg>
      <strong>Friendly &amp; Reliable Service</strong>
    </li>
  </ul>
</section>

</body>
</html>
```